Web Design for Harbor Ledger Allies

Harbor Ledger Allies needs the photoshop files for a simple, clean and professional website design. The company is building a network of bookkeepers/accountants to handle outsourced bookkeeping services for start ups and small businesses. It needs to both attract bookkeepers to become partners and give clients confidence in the professional network. The partners will use products like Tallymint Web, Brightfolio.example and PennyTrim.example for start ups, as well as help with tasks using the clients existing accounting software.

A home and subpage design is needed. I'll award the work based on the home design. The minor subpage changes can be worked out in the workroom stage.

The pages for the navigation will be: Home, Services, Locations, Partners, FAQ, Contact

```html
<!DOCTYPE html>
<html lang="en">
<head>
<meta charset="utf-8">
<title>Harbor Ledger Allies</title>
<link rel="stylesheet" href="https://fonts.googleapis.com/css2?family=Arimo:wght@400;700&family=Roboto+Condensed:wght@400;700&display=swap">
<style>
  :root {
    --ink: #2f2f2f;
    --grey: #5f5f5f;
    --mid: #777777;
    --blue: #1ba3dc;
    --black: #0d0d0d;
    --white: #ffffff;
    --hatch: #e4e4e4;
    --rule: #e6e6e6;
  }
  * { box-sizing: border-box; margin: 0; padding: 0; }
  html, body { width: 1004px; height: 1200px; overflow: hidden; }
  body { position: relative; background: var(--white); font-family: "Arimo", Arial, sans-serif; color: var(--ink); }

  .top-bar { position: absolute; left: 0; top: 0; width: 1004px; height: 18px; background: var(--black); border-bottom: 3px solid var(--blue); }

  .brand { position: absolute; display: flex; align-items: center; gap: 10px; }
  .brand-dot { width: 14px; height: 14px; border-radius: 50%; background: var(--blue); flex: none; }
  .brand-name { font-family: "Roboto Condensed", Arial, sans-serif; font-weight: 700; color: var(--grey); text-transform: uppercase; line-height: 0.95; }
  .site-header .brand { left: 117px; top: 58px; }
  .site-header .brand-name { font-size: 19px; }

  .main-nav { position: absolute; right: 101px; top: 90px; display: flex; align-items: center; font-family: "Roboto Condensed", Arial, sans-serif; font-weight: 700; font-size: 17px; color: var(--ink); text-transform: uppercase; }
  .main-nav .sep { color: var(--blue); margin: 0 12px; font-weight: 400; }

  .hero { position: absolute; left: 115px; top: 132px; width: 788px; height: 355px; overflow: hidden;
    background: radial-gradient(ellipse 240px 180px at 270px 190px, #7fc8d8 0%, #3a7f95 30%, #2a3e48 60%, transparent 100%),
                linear-gradient(90deg, #2b3036 0%, #3a3a3c 50%, #3c3c3e 100%); }
  .hero .brand { left: 470px; top: 232px; }
  .hero .brand-name { font-size: 28px; color: #9a9a9a; }
  .hero .brand-dot { width: 20px; height: 20px; }
  .slider-dots { position: absolute; right: 14px; bottom: 11px; display: flex; gap: 6px; }
  .slider-dots span { width: 20px; height: 3px; background: var(--white); }
  .slider-dots span.is-dim { background: #555; }

  .features { position: absolute; left: 119px; top: 548px; width: 800px; }
  .feature { position: absolute; top: 0; width: 240px; }
  .feature h2 { display: flex; align-items: center; gap: 12px; font-family: "Arimo", Arial, sans-serif; font-weight: 700; font-size: 20px; color: var(--grey); text-transform: uppercase; height: 30px; }
  .feature h2 em { font-style: normal; color: var(--blue); }
  .feature p { margin-top: 15px; font-size: 10.6px; line-height: 15.3px; color: var(--ink); }
  .more { display: flex; align-items: center; gap: 10px; margin-top: 13px; font-family: "Roboto Condensed", Arial, sans-serif; font-weight: 700; font-size: 11px; color: var(--ink); text-transform: uppercase; letter-spacing: -0.2px; }

  .section-title { position: absolute; left: 115px; top: 800px; width: 788px; height: 24px; display: flex; align-items: center; gap: 16px; }
  .section-title .band { flex: 1; height: 24px; background: var(--hatch); }
  .section-title h2 { font-family: "Roboto Condensed", Arial, sans-serif; font-weight: 700; font-size: 21px; color: var(--ink); text-transform: uppercase; }

  .partner { position: absolute; top: 862px; width: 170px; text-align: center; }
  .partner-name { height: 76px; display: flex; align-items: center; justify-content: center; gap: 8px; font-family: "Arimo", Arial, sans-serif; font-weight: 700; font-size: 24px; color: #4a4a4a; letter-spacing: -0.5px; border-bottom: 1px solid var(--rule); }
  .partner-name .mark { width: 12px; height: 12px; background: #6a6a6a; }
  .partner .more { justify-content: center; margin-top: 10px; letter-spacing: 0.6px; }

  .site-footer { position: absolute; left: 0; top: 1066px; width: 1004px; height: 134px; background: var(--black); border-top: 3px solid var(--blue); }
  .site-footer .brand { left: 93px; top: 36px; }
  .site-footer .brand-name { font-size: 15px; color: #8a8a8a; }
  .site-footer .brand-dot { width: 12px; height: 12px; }
  .footer-divider { position: absolute; left: 310px; top: 32px; width: 1px; height: 45px; background: #3a3a3a; }
  .footer-nav { position: absolute; left: 336px; top: 38px; display: flex; font-size: 10.5px; color: var(--white); text-transform: uppercase; }
  .footer-nav .sep { color: var(--blue); margin: 0 13px; }
  .copyright { position: absolute; left: 336px; top: 68px; font-size: 10px; color: #cfcfcf; text-transform: uppercase; }
</style>
</head>
<body>
  <div class="top-bar"></div>

  <header class="site-header">
    <div class="brand">
      <span class="brand-dot"></span>
      <span class="brand-name">Harbor Ledger<br>Allies</span>
    </div>
    <nav class="main-nav">
      <span>Home</span><span class="sep">|</span>
      <span>Services</span><span class="sep">|</span>
      <span>Locations</span><span class="sep">|</span>
      <span>Partners</span><span class="sep">|</span>
      <span>FAQ</span><span class="sep">|</span>
      <span>Contact</span>
    </nav>
  </header>

  <section class="hero" role="img" aria-label="Photo of open hands holding glowing devices, a world map and message icons on a dark background">
    <div class="brand">
      <span class="brand-dot"></span>
      <span class="brand-name">Harbor Ledger<br>Allies</span>
    </div>
    <div class="slider-dots"><span class="is-dim"></span><span></span><span></span><span></span></div>
  </section>

  <section class="features">
    <article class="feature" style="left:0">
      <h2><svg width="28" height="28" viewBox="0 0 28 28"><circle cx="11" cy="11" r="8" fill="none" stroke="#8a8a8a" stroke-width="4"/><line x1="17" y1="17" x2="25" y2="25" stroke="#8a8a8a" stroke-width="5" stroke-linecap="round"/></svg>Sample <em>Text</em></h2>
      <p>Lorem ipsum dolor sit amet, consectetur adipiscing elit. Mauris fringilla nibh vel neque fringilla, quis mattis lorem condimentum. Etiam rhoncus faucibus eros ut egestas. Nulla nulla est, congue in semper vitae, blandit eget mi. Nam posuere laoreet eros in luctus. Vivamus pharetra justo ac risus hendrerit sodales.</p>
      <div class="more"><svg width="14" height="10" viewBox="0 0 14 10"><path d="M1 1l4 4-4 4M7 1l4 4-4 4" fill="none" stroke="#1ba3dc" stroke-width="2.2"/></svg>Find out more</div>
    </article>
    <article class="feature" style="left:274px">
      <h2><svg width="28" height="28" viewBox="0 0 28 28"><circle cx="11" cy="11" r="8" fill="none" stroke="#8a8a8a" stroke-width="4"/><line x1="17" y1="17" x2="25" y2="25" stroke="#8a8a8a" stroke-width="5" stroke-linecap="round"/></svg>Sample <em>Text</em></h2>
      <p>Lorem ipsum dolor sit amet, consectetur adipiscing elit. Mauris fringilla nibh vel neque fringilla, quis mattis lorem condimentum. Etiam rhoncus faucibus eros ut egestas. Nulla nulla est, congue in semper vitae, blandit eget mi. Nam posuere laoreet eros in luctus. Vivamus pharetra justo ac risus hendrerit sodales.</p>
      <div class="more"><svg width="14" height="10" viewBox="0 0 14 10"><path d="M1 1l4 4-4 4M7 1l4 4-4 4" fill="none" stroke="#1ba3dc" stroke-width="2.2"/></svg>Find out more</div>
    </article>
    <article class="feature" style="left:538px">
      <h2><svg width="28" height="28" viewBox="0 0 28 28"><circle cx="11" cy="11" r="8" fill="none" stroke="#8a8a8a" stroke-width="4"/><line x1="17" y1="17" x2="25" y2="25" stroke="#8a8a8a" stroke-width="5" stroke-linecap="round"/></svg>Sample <em>Text</em></h2>
      <p>Lorem ipsum dolor sit amet, consectetur adipiscing elit. Mauris fringilla nibh vel neque fringilla, quis mattis lorem condimentum. Etiam rhoncus faucibus eros ut egestas. Nulla nulla est, congue in semper vitae, blandit eget mi. Nam posuere laoreet eros in luctus. Vivamus pharetra justo ac risus hendrerit sodales.</p>
      <div class="more"><svg width="14" height="10" viewBox="0 0 14 10"><path d="M1 1l4 4-4 4M7 1l4 4-4 4" fill="none" stroke="#1ba3dc" stroke-width="2.2"/></svg>Find out more</div>
    </article>
  </section>

  <div class="section-title"><span class="band"></span><h2>Partners</h2><span class="band"></span></div>

  <div class="partner" style="left:115px">
    <div class="partner-name"><span class="mark"></span>Brightfolio</div>
    <div class="more"><svg width="14" height="10" viewBox="0 0 14 10"><path d="M1 1l4 4-4 4M7 1l4 4-4 4" fill="none" stroke="#1ba3dc" stroke-width="2.2"/></svg>View Partner</div>
  </div>
  <div class="partner" style="left:307px">
    <div class="partner-name"><span class="mark"></span>Brightfolio</div>
    <div class="more"><svg width="14" height="10" viewBox="0 0 14 10"><path d="M1 1l4 4-4 4M7 1l4 4-4 4" fill="none" stroke="#1ba3dc" stroke-width="2.2"/></svg>View Partner</div>
  </div>
  <div class="partner" style="left:495px">
    <div class="partner-name"><span class="mark"></span>Brightfolio</div>
    <div class="more"><svg width="14" height="10" viewBox="0 0 14 10"><path d="M1 1l4 4-4 4M7 1l4 4-4 4" fill="none" stroke="#1ba3dc" stroke-width="2.2"/></svg>View Partner</div>
  </div>
  <div class="partner" style="left:688px">
    <div class="partner-name"><span class="mark"></span>Brightfolio</div>
    <div class="more"><svg width="14" height="10" viewBox="0 0 14 10"><path d="M1 1l4 4-4 4M7 1l4 4-4 4" fill="none" stroke="#1ba3dc" stroke-width="2.2"/></svg>View Partner</div>
  </div>

  <footer class="site-footer">
    <div class="brand">
      <span class="brand-dot"></span>
      <span class="brand-name">Harbor Ledger<br>Allies</span>
    </div>
    <div class="footer-divider"></div>
    <nav class="footer-nav">
      <span>Home</span><span class="sep">|</span>
      <span>Services</span><span class="sep">|</span>
      <span>Locations</span><span class="sep">|</span>
      <span>Partners</span><span class="sep">|</span>
      <span>FAQ</span><span class="sep">|</span>
      <span>Contact</span>
    </nav>
    <p class="copyright">© 2014 Harbor Ledger Allies. All rights reserved.</p>
  </footer>
</body>
</html>
```